Kestrel Valley Alpine Riders Society needs a business card design

We need a business card design for our newly incorporated KVARS. We are helping the NZ Chinese community, as well as everyone else, to organise ski & snowboarding trips, training, and equipments. The design should be creative, energetic, young and vibrant.

Industry/Entity Type

Social Club

Contact Information for Business Card

Logo; Kestrel Valley Alpine Riders Society; Name: Oliver Brandt; Position: President; Address: 42 Marwick Rd, Epsom, Auckland 1051; Mobile: 020 7826 1957; Email: oliver@kvars-club.example; Web: www.kvars-club.example

Requirements
Must have
• 1, The text "Kestrel Valley Alpine Riders Society" should be put together with the supplied logo file to form a new complete logo combination.
• 2, Final design files should be in Adobe Illustrator format and all text must be editable.
Nice to have
• two or three colours

```html
<!DOCTYPE html>
<html lang="en">
<head>
<meta charset="utf-8">
<title>KVARS – Business Card</title>
<link rel="stylesheet" href="https://fonts.googleapis.com/css2?family=Quicksand:wght@400;700&display=swap">
<style>
  :root {
    --paper: #ffffff;
    --ink-grey: #8c8c8c;
    --brand-blue: #2f86d6;
    --ice-light: #e6f8fb;
    --ice-mid: #7fd3dc;
    --ice-deep: #2d8fa3;
    --night: #1c2b3a;
    --label-wash: rgba(255, 255, 255, 0.72);
  }
  html, body {
    margin: 0;
    padding: 0;
    overflow: hidden;
    background: var(--paper);
  }
  .card {
    position: relative;
    width: 1200px;
    height: 750px;
    background: var(--paper);
    overflow: hidden;
    font-family: "Quicksand", sans-serif;
    font-weight: 400;
    color: var(--ink-grey);
  }
  .hero-band {
    position: absolute;
    inset: 0;
    width: 1200px;
    height: 750px;
  }
  .brand {
    position: absolute;
    left: 22px;
    top: 28px;
  }
  .brand-mark {
    display: flex;
    align-items: center;
    gap: 16px;
  }
  .brand-dot {
    width: 42px;
    height: 42px;
    border-radius: 50%;
    background: var(--brand-blue);
  }
  .brand-name {
    font-weight: 700;
    font-size: 110px;
    line-height: 1;
    letter-spacing: 2px;
    color: var(--brand-blue);
  }
  .brand-fullname {
    margin: 6px 0 0 2px;
    font-weight: 700;
    font-size: 23px;
    line-height: 1.2;
    color: var(--brand-blue);
  }
  .contact {
    position: absolute;
    left: 14px;
    top: 248px;
    line-height: 1;
  }
  .contact-name,
  .contact-role {
    font-size: 52px;
    margin: 0 0 8px;
  }
  .contact-phone {
    font-size: 38px;
    margin: 4px 0 0;
  }
  .services {
    position: absolute;
    right: 12px;
    top: 330px;
    text-align: right;
    font-size: 44px;
    line-height: 46px;
    margin: 0;
    padding: 0;
    list-style: none;
  }
  .services .highlight {
    display: inline-block;
    background: var(--label-wash);
    padding: 0 2px 2px 8px;
  }
  .address {
    position: absolute;
    right: 12px;
    top: 540px;
    text-align: right;
    font-size: 40px;
    line-height: 48px;
    font-style: normal;
    margin: 0;
  }
</style>
</head>
<body>
  <div class="card">
    <svg class="hero-band" viewBox="0 0 1200 750" role="img" aria-label="Illustration of a snowboarder in goggles and a green-and-white jacket carving through sparkling powder snow">
      <defs>
        <linearGradient id="snow-glow" x1="0" y1="0" x2="1" y2="1">
          <stop offset="0" stop-color="var(--ice-light)"/>
          <stop offset="0.35" stop-color="var(--ice-mid)"/>
          <stop offset="0.65" stop-color="var(--ice-deep)"/>
          <stop offset="1" stop-color="var(--night)"/>
        </linearGradient>
      </defs>
      <polygon points="680,0 1131,0 643,750 191,750" fill="url(#snow-glow)"/>
    </svg>

    <div class="brand">
      <div class="brand-mark">
        <span class="brand-dot"></span>
        <span class="brand-name">KVARS</span>
      </div>
      <p class="brand-fullname">Kestrel Valley Alpine Riders Society</p>
    </div>

    <div class="contact">
      <p class="contact-name">Oliver Brandt</p>
      <p class="contact-role">President</p>
      <p class="contact-phone">Mobile: 020 7826 1957</p>
    </div>

    <ul class="services">
      <li>Ski &amp;</li>
      <li><span class="highlight">Snowboarding trips</span></li>
      <li>Training</li>
      <li>Equipments</li>
    </ul>

    <address class="address">
      42 Marwick Rd, Epsom<br>
      Auckland 1051.<br>
      oliver@kvars-club.example<br>
      www.kvars-club.example
    </address>
  </div>
</body>
</html>
```